Revamp QuillStoneKit.com

https://quillstonekit.com/ needs a revamp. We like the general style and colors of the site, we just want to modernize the landing page, product page, view cart page, and the final confirm page.

I'm just looking for the PSD (Photoshop files) as the deliverable.

Quick Summary
Please redesign the following Pages:
1) https://quillstonekit.com/
2) https://quillstonekit.com/rubberTracks/QuillStoneKit/400x725nx70.php (product Page)
3) https://quillstonekit.com/viewCart.php (view cart - Add something to cart to see)
4) https://quillstonekit.com/confirmShoppingCart.php (confirm cart - Add something to cart to see)

```html
<!DOCTYPE html>
<html lang="en">
<head>
<meta charset="utf-8">
<title>QuillStoneKit – Cart</title>
<link href="https://fonts.googleapis.com/css2?family=Open+Sans:wght@300;400;600;700&display=swap" rel="stylesheet">
<style>
:root{
  --gold:#d9b24c;
  --ink:#222;
  --text:#444;
  --muted:#888;
  --light:#f3f4f6;
  --field:#f0eded;
  --line:#e6e6e6;
  --dark:#2a2a2a;
}
*{margin:0;padding:0;box-sizing:border-box}
html,body{width:724px;height:1200px;overflow:hidden;background:#fff}
body{position:relative;font-family:"Open Sans",sans-serif;color:var(--text)}
.abs{position:absolute}
.topbar{left:0;top:0;width:724px;height:30px;background:#000;color:#fff;font-weight:700;font-size:12px;letter-spacing:.3px;text-align:center;line-height:30px}
.header{left:0;top:30px;width:724px;height:68px;background:var(--light)}
.nav a{position:absolute;top:8px;font-size:8px;color:var(--text);text-decoration:none}
.nav a.active{color:var(--gold)}
.currency{right:69px;top:9px;font-size:7px;color:var(--text)}
.brand{left:68px;top:31px;font-size:17px;font-weight:700;color:var(--ink);letter-spacing:-.2px;display:flex;align-items:center;gap:5px}
.brand i{width:10px;height:10px;background:var(--gold);display:block}
.hotline{right:202px;top:29px;text-align:right}
.hotline b{display:block;color:var(--gold);font-size:11.5px;font-weight:600}
.hotline span{font-size:9px;color:var(--muted);font-weight:300}
.cart-link{left:603px;top:41px;display:flex;align-items:flex-end;gap:4px;font-size:10px;color:var(--text)}
.cart-link .badge{position:absolute;left:8px;top:-7px;width:12px;height:12px;border-radius:50%;background:var(--gold);color:#fff;font-size:6.5px;text-align:center;line-height:12px}
.cats{left:68px;top:108px;width:131px;height:25px;background:var(--gold);color:#fff;font-size:8px;font-weight:600;line-height:25px;padding-left:8px}
.search{left:220px;top:108px;width:360px;height:25px;border:1px solid var(--ink);display:flex;align-items:center;gap:6px;padding-left:9px;font-size:7.5px;color:var(--text)}
.search-btn{left:580px;top:108px;width:76px;height:25px;background:var(--gold);color:#fff;font-size:8.5px;text-align:center;line-height:25px}
.crumbs{left:0;top:142px;width:724px;height:17px;background:var(--light);font-size:6.5px;color:var(--muted);line-height:17px;padding-left:67px}
.page-title{left:0;top:172px;width:724px;text-align:center;font-size:15px;font-weight:600;color:#333}
.card{background:#fff;box-shadow:0 1px 6px rgba(0,0,0,.13)}
.cart-table{left:67px;top:206px;width:585px;height:224px}
.th,.td{position:absolute;transform:translateX(-50%);white-space:nowrap}
.th{top:14px;font-size:7px;color:var(--text)}
.rule{position:absolute;left:8px;width:570px;height:1px;background:var(--line)}
.rule.head{background:#333;top:28px}
.thumb{position:absolute;left:44px;width:46px;height:31px;background:linear-gradient(135deg,#f1eeec,#e7e3e1)}
.pname{font-size:5.5px;color:#222;text-align:center;line-height:1.15}
.pname small{display:block;font-size:4.5px;color:var(--muted)}
.price{font-size:9px;color:#222}
.total{font-size:9px;color:var(--gold)}
.qty{display:flex;align-items:center;gap:7px;font-size:9px;color:#555}
.qty .box{width:36px;height:16px;background:#e9ecef;border:1px solid #d5d8db;font-size:6.5px;font-weight:700;color:#222;text-align:center;line-height:14px}
.links{position:absolute;top:190px;font-size:5.5px;color:var(--gold);display:flex;gap:5px;align-items:center}
.panel{top:458px;width:183px}
.panel h3{position:absolute;left:22px;top:16px;font-size:8.5px;font-weight:400;color:#222}
.panel p.sub{position:absolute;left:22px;top:37px;font-size:5.5px;color:var(--muted)}
.label{position:absolute;left:22px;font-size:6.5px;color:#222}
.select{position:absolute;left:22px;width:139px;height:21px;background:var(--field);font-size:5.5px;color:var(--muted);line-height:21px;padding-left:7px}
.select svg{position:absolute;right:7px;top:8px}
.btn-outline{position:absolute;left:22px;top:205px;width:139px;height:21px;border:1px solid #333;font-size:7px;color:#222;text-align:center;line-height:19px}
.note-area{position:absolute;left:20px;top:54px;width:139px;height:172px;background:var(--field)}
.sum-row{position:absolute;left:22px;right:23px;display:flex;justify-content:space-between;align-items:center;color:#222}
.agree{position:absolute;left:22px;top:73px;font-size:7px;color:#333;display:flex;gap:4px;align-items:center}
.btn-dark{position:absolute;left:22px;top:99px;width:141px;height:21px;background:var(--dark);color:#fff;font-size:7px;text-align:center;line-height:21px}
.callband{left:0;top:753px;width:724px;height:63px;background:var(--gold);color:#fff}
.callband .txt{position:absolute;left:153px;top:18px;font-size:15.5px;font-weight:600}
.callband .num{position:absolute;left:446px;top:10px;font-size:26px;font-weight:700}
.f-brand{left:67px;top:862px;font-size:16px;font-weight:700;color:var(--ink);display:flex;align-items:center;gap:5px}
.f-brand i{width:11px;height:11px;background:var(--gold);display:block}
.legal{left:67px;top:936px;width:203px;font-size:7px;line-height:12px;color:#333}
.pay{left:68px;top:1055px;display:flex;gap:2px}
.pay span{width:35px;height:21px;border-radius:2px;display:block}
.vline{left:287px;top:836px;width:1px;height:248px;background:var(--line)}
.subscribe{left:320px;top:873px;font-size:8.5px;font-weight:600;color:#222;letter-spacing:.2px}
.email{left:468px;top:869px;width:187px;height:23px;border:1px solid var(--line);font-size:7px;color:var(--muted);padding-left:6px;line-height:21px}
.email svg{position:absolute;right:7px;top:6px}
.hline{height:1px;background:var(--line)}
.col h4{font-size:8.5px;font-weight:600;color:#222;margin-bottom:8px;letter-spacing:.2px}
.col li{list-style:none;font-size:7px;color:var(--muted);height:16.6px}
.contact li{display:flex;gap:6px;align-items:center}
.follow{left:239px;top:1116px;font-size:11px;font-weight:300;color:var(--muted)}
.social{top:1106px;width:28px;height:28px;border:1px solid #444;border-radius:50%}
.copyright{left:0;top:1157px;width:724px;height:43px;background:var(--light);text-align:center;line-height:43px;font-size:9px;color:#444;font-weight:300}
</style>
</head>
<body>

<div class="abs topbar">FREE SHIPPING IN THE USA</div>

<header class="abs header">
  <nav class="nav">
    <a class="active" style="left:68px">Home</a>
    <a style="left:104px">About Us</a>
    <a style="left:159px">Shop</a>
    <a style="left:195px">Contact Us</a>
  </nav>
  <div class="abs currency">USD ⌄</div>
  <div class="abs brand"><i></i>QuillStoneKit</div>
  <div class="abs hotline"><b>(+1)123-456-789</b><span>Timing 10:00 to 18:00 (Mon-Sat) Free By United States</span></div>
  <div class="abs cart-link">
    <svg width="14" height="14" viewBox="0 0 24 24"><path fill="#111" d="M7 18a2 2 0 100 4 2 2 0 000-4zm10 0a2 2 0 100 4 2 2 0 000-4zM1 2v2h2l3.6 7.6-1.4 2.4c-.6 1.3.3 3 1.8 3h12v-2H7.4l1.1-2h7.5c.8 0 1.4-.4 1.7-1l3.6-6.5A1 1 0 0020.4 4H5.2l-.9-2H1z"/></svg>
    <span class="badge">0</span>My Cart
  </div>
</header>

<div class="abs cats">CATEGORIES</div>
<div class="abs search">
  <svg width="13" height="13" viewBox="0 0 24 24"><circle cx="10" cy="10" r="7" fill="none" stroke="#d9b24c" stroke-width="2"/><path d="M15 15l6 6" stroke="#d9b24c" stroke-width="2"/></svg>
  Search Product Here...
</div>
<div class="abs search-btn">SEARCH</div>

<div class="abs crumbs">Home / cart</div>
<h1 class="abs page-title">CART</h1>

<section class="abs card cart-table">
  <span class="th" style="left:57px">Product</span>
  <span class="th" style="left:137px">Name</span>
  <span class="th" style="left:223px">Price</span>
  <span class="th" style="left:302px">Quantity</span>
  <span class="th" style="left:419px">Total</span>
  <span class="th" style="left:521px">Remove</span>
  <div class="rule head"></div>

  <!-- row 1 -->
  <div class="thumb" role="img" aria-label="Rubber track product photo" style="top:38px"></div>
  <div class="td pname" style="left:145px;top:46px">Rubber Track<small>(320x86x50)</small></div>
  <div class="td price" style="left:230px;top:46px">$250.00</div>
  <div class="td qty" style="left:319px;top:46px">–<span class="box">1</span>+</div>
  <div class="td total" style="left:426px;top:46px">$250.00</div>
  <svg class="td" style="left:516px;top:48px" width="11" height="11" viewBox="0 0 10 10"><path d="M1 1l8 8M9 1l-8 8" stroke="#222" stroke-width="1.3"/></svg>
  <div class="rule" style="top:77px"></div>

  <!-- row 2 -->
  <div class="thumb" role="img" aria-label="Rubber track product photo" style="top:85px"></div>
  <div class="td pname" style="left:145px;top:94px">Rubber Track<small>(320x86x50)</small></div>
  <div class="td price" style="left:230px;top:94px">$250.00</div>
  <div class="td qty" style="left:319px;top:94px">–<span class="box">1</span>+</div>
  <div class="td total" style="left:426px;top:94px">$250.00</div>
  <svg class="td" style="left:516px;top:96px" width="11" height="11" viewBox="0 0 10 10"><path d="M1 1l8 8M9 1l-8 8" stroke="#222" stroke-width="1.3"/></svg>
  <div class="rule" style="top:124px"></div>

  <!-- row 3 -->
  <div class="thumb" role="img" aria-label="Rubber track product photo" style="top:133px"></div>
  <div class="td pname" style="left:145px;top:141px">Rubber Track<small>(320x86x50)</small></div>
  <div class="td price" style="left:230px;top:141px">$250.00</div>
  <div class="td qty" style="left:319px;top:141px">–<span class="box">1</span>+</div>
  <div class="td total" style="left:426px;top:141px">$250.00</div>
  <svg class="td" style="left:516px;top:143px" width="11" height="11" viewBox="0 0 10 10"><path d="M1 1l8 8M9 1l-8 8" stroke="#222" stroke-width="1.3"/></svg>
  <div class="rule" style="top:172px"></div>

  <div class="links" style="left:45px">↩ CONTINUE SHOPPING</div>
  <div class="links" style="left:395px">▮ CLEAR SHOPPING CART &nbsp;⟳ UPDATE CART</div>
</section>

<section class="abs card panel" style="left:67px;height:243px">
  <h3>ESTIMATE SHIPPING AND TAX</h3>
  <p class="sub">Enter your destination to get a shipping estimate</p>
  <span class="label" style="top:60px">COUNTARY *</span>
  <div class="select" style="top:77px">United States<svg width="7" height="5" viewBox="0 0 7 5"><path d="M.5 .5l3 3 3-3" fill="none" stroke="#555"/></svg></div>
  <span class="label" style="top:106px">STATE/PROVINCE *</span>
  <div class="select" style="top:122px">United States<svg width="7" height="5" viewBox="0 0 7 5"><path d="M.5 .5l3 3 3-3" fill="none" stroke="#555"/></svg></div>
  <span class="label" style="top:152px">ZIP/POSTAL CODE</span>
  <div class="select" style="top:168px">United States<svg width="7" height="5" viewBox="0 0 7 5"><path d="M.5 .5l3 3 3-3" fill="none" stroke="#555"/></svg></div>
  <div class="btn-outline">CALCULATE SHIPPING</div>
</section>

<section class="abs card panel" style="left:270px;height:243px">
  <h3>NOTE</h3>
  <p class="sub">Add special instructions for your order</p>
  <div class="note-area"></div>
</section>

<section class="abs card panel" style="left:472px;height:147px">
  <div class="sum-row" style="top:16px;font-size:8.5px;font-weight:600"><span>SUBTOTAL</span><span>$12,00.00</span></div>
  <div class="sum-row" style="top:40px"><span style="font-size:8.5px;font-weight:600">GRAND TOTAL</span><span style="font-size:12px;font-weight:700;color:var(--gold)">$18,00.00</span></div>
  <div class="agree"><svg width="7" height="7" viewBox="0 0 7 7"><rect width="7" height="7" rx="1" fill="#d9b24c"/><path d="M1.5 3.5l1.4 1.4 2.6-2.8" fill="none" stroke="#fff"/></svg>I agree with the terms and conditions</div>
  <div class="btn-dark">PROCEED TO CHECKOUT</div>
</section>

<section class="abs callband">
  <svg class="abs" style="left:115px;top:20px" width="24" height="24" viewBox="0 0 24 24"><path fill="#fff" d="M6.6 10.8a15 15 0 006.6 6.6l2.2-2.2c.3-.3.7-.4 1-.2 1.1.4 2.3.6 3.6.6.6 0 1 .4 1 1V20c0 .6-.4 1-1 1A17 17 0 013 4c0-.6.4-1 1-1h3.5c.6 0 1 .4 1 1 0 1.3.2 2.5.6 3.6.1.3 0 .7-.2 1z"/></svg>
  <span class="txt">if you have any question please call us</span>
  <span class="num">123-456-7890</span>
</section>

<footer>
  <div class="abs f-brand"><i></i>QuillStoneKit</div>
  <p class="abs legal">QuillStoneKit™, Bramblecat®, Casewell®, Crawlerton®, Crt®, Trench Wren®, Gelvin®, IHX®, JVR®, Jon Dearborn®, Kobrano®, Kuvara®, Moravka®, Mustrel®, New Hollis®, Takemara®, Terrin®, Vermond®, and Yarrow® (hereafter, collectively referred to as "Marks") are trademarks and/or registered trademarks of their respective owners, who are individually identified in our Legal Di</p>
  <div class="abs pay" role="img" aria-label="Accepted payment cards">
    <span style="background:#e8ecf5;border:1px solid #c9d0e2"></span>
    <span style="background:#e5463a"></span>
    <span style="background:#f3a24a"></span>
    <span style="background:#3a8fd8"></span>
  </div>
  <div class="abs vline"></div>

  <div class="abs subscribe">SUBSCRIBE TO NEWSLETTER</div>
  <div class="abs email">Enter your email address
    <svg width="10" height="10" viewBox="0 0 24 24"><path fill="#d9b24c" d="M2 11l20-9-7 20-3-8z"/></svg>
  </div>
  <div class="abs hline" style="left:321px;top:915px;width:335px"></div>

  <div class="abs col" style="left:320px;top:948px">
    <h4>CATEGORIES</h4>
    <ul><li>Category 1</li><li>Category 2</li><li>Category 3</li><li>Category 4</li><li>Category 5</li></ul>
  </div>
  <div class="abs col" style="left:421px;top:948px">
    <h4>QUICK LINK</h4>
    <ul><li>Home</li><li>About</li><li>Privacy Policy</li><li>Terms of Service</li><li>Contact</li></ul>
  </div>
  <div class="abs col contact" style="left:524px;top:950px">
    <h4>CONTACT US</h4>
    <ul>
      <li><svg width="7" height="9" viewBox="0 0 12 16"><path fill="#d9b24c" d="M6 0a6 6 0 00-6 6c0 4.5 6 10 6 10s6-5.5 6-10a6 6 0 00-6-6zm0 8.5A2.5 2.5 0 116 3.5a2.5 2.5 0 010 5z"/></svg>Lorem ipsum is dolor amet</li>
      <li><svg width="8" height="8" viewBox="0 0 24 24"><path fill="#d9b24c" d="M6.6 10.8a15 15 0 006.6 6.6l2.2-2.2c.3-.3.7-.4 1-.2 1.1.4 2.3.6 3.6.6.6 0 1 .4 1 1V20c0 .6-.4 1-1 1A17 17 0 013 4c0-.6.4-1 1-1h3.5c.6 0 1 .4 1 1 0 1.3.2 2.5.6 3.6.1.3 0 .7-.2 1z"/></svg>(+1)123-456-789</li>
      <li><svg width="9" height="7" viewBox="0 0 18 12"><rect width="18" height="12" fill="#d9b24c"/><path d="M0 0l9 7 9-7" fill="none" stroke="#fff"/></svg>info@example.com</li>
    </ul>
  </div>

  <div class="abs hline" style="left:67px;top:1098px;width:589px"></div>
  <div class="abs follow">FOLLOW US:</div>
  <span class="abs social" style="left:329px" role="img" aria-label="Social profile link"></span>
  <span class="abs social" style="left:371px" role="img" aria-label="Social profile link"></span>
  <span class="abs social" style="left:414px" role="img" aria-label="Social profile link"></span>
  <span class="abs social" style="left:456px" role="img" aria-label="Social profile link"></span>

  <div class="abs copyright">© 2020 QUILLSTONEKIT, LLC. ALL RIGHTS ARE RESEVED.</div>
</footer>

</body>
</html>
```